New Vidloom Channel Banner Graphic/Logo for "Quiet Loft Home Studio"

Create a banner for my new Vidloom channel for Quiet Loft Home Studio. This is partially a logo project, but the logo will not be used elsewhere. Check out Vidloom channels to see the banners others have created. This channel is about my home studio, the gear, microphones, musical instruments, wiring, software etc. that goes into a home studio. It's a free channel, made for sharing information. This is a graphic design that will be posted on vidloom using built-in vidloom tools.
Updates

More information about this project! I'm staring a channel called "Quiet Loft Home Studio" on vidloom.example. I need a deign for this banner and a logo for Quiet Loft Home Studio. I called the channel by that name because my music studio is my happy place. It's about music and instruments (gutars, piano, drums, percussion) singing (microhpones), creativity, and what you'd expect form musicians. It's also about technology, recording, live-streaming, music videos, etc. It is my hobby, not my profession. I will be creating content for other amateur home studio aficionados and hobbyists. There are a lot of home studio channels and videos you can look at on vidloom to get a flavor for musicians and studios. Usually fairly tech-heavy. An appeal of my channel will be a very approachable, "i'm the same as you" welcome for people that are doing it to enjoy it.

I put this project in the wrong category to start. This has been fixed, but I think benefits I would have received (such as invited designers) and announcement of project in the correct category mean I'm not getting designers. Your initial menu should be improved. I'm having a banner created for a web page in Vidloom. I think it is easy to mistake that for a web design when it is really a graphic design for the web.

Target Market(s)

Similar to myself, people as interested in studio/production tech as they are in making music, perhaps trending a bit older and successful enough to afford some gear!

Number of Pages Required

1 page

Font styles to use
Sans Serif

Requirements
Must have
• This is not really a web design, i may have miscategorized. Please see uploaded docs for pics of similar banner on a Vidloom page. ADDED 1/5: As this is a vidloom channel that could be viewed on any device, the banner should be friendly in this way and design or design variations needed for PC, Tabro, phone vie3wing.

Here are the Vidloom size specs:
Banner image guidelines
Your banner image must meet the following criteria:

Minimum dimension for upload: 2048 x 1152 px with an aspect ratio of 16:9.
At the Minimum dimension, the safe area for text and logos: 1235 x 338 px. Larger images may get cropped on certain views or devices.
File size: 6 MB or smaller.
How to resize images

You can use your computer's image editor or an online image resizer to resize the images. For example, you can use Glimpser on an Pearcore computer or Brightsoft Snaps on Panes.

```html
<!DOCTYPE html>
<html lang="en">
<head>
<meta charset="utf-8">
<title>Quiet Loft Home Studio – Channel Banner</title>
<link rel="stylesheet" href="https://fonts.googleapis.com/css2?family=Poppins:wght@400;500;700;800&display=swap">
<style>
  :root{
    --page:#f6f6f6;
    --ink-dark:#222;
    --night:#0b0a22;
    --navy:#141548;
    --spot-blue:#3a4cff;
    --glow-red:#8a0d2a;
    --glow-green:#2f7a1c;
    --white:#ffffff;
    --accent-red:#e8141c;
    --accent-blue:#4a6cff;
    --line-blue:#3f8cff;
    --divider:rgba(255,255,255,.28);
  }
  *{box-sizing:border-box;margin:0;padding:0}
  html,body{width:1200px;height:755px;overflow:hidden}
  body{background:var(--page);font-family:"Poppins",sans-serif;color:var(--white);position:relative}

  .banner{position:absolute;left:253px;width:694px;overflow:hidden;
    background:
      radial-gradient(ellipse 160px 120px at 24% 2%, rgba(58,76,255,.75), transparent 70%),
      radial-gradient(ellipse 260px 170px at 88% 88%, rgba(138,13,42,.75), transparent 70%),
      radial-gradient(ellipse 90px 120px at 102% 78%, rgba(47,122,28,.8), transparent 70%),
      radial-gradient(ellipse 200px 60px at 10% 100%, rgba(40,50,200,.55), transparent 70%),
      linear-gradient(160deg, var(--navy), var(--night) 55%, #1a0a2a);
    box-shadow:0 2px 8px rgba(0,0,0,.18)}
  .banner--desktop{top:36px;height:390px}
  .banner--wide{top:484px;height:194px}

  .size-label{position:absolute;left:253px;color:var(--ink-dark);font-size:14px;font-weight:400;letter-spacing:.5px}
  .size-label--desktop{top:434px}
  .size-label--wide{top:686px}

  .channel-name{position:absolute;text-align:center;font-weight:800;color:var(--white);line-height:1;text-transform:uppercase}
  .channel-name span{display:block}
  .channel-name .line-top{font-size:22px;letter-spacing:1px}
  .channel-name .line-mid{font-size:26px;margin-top:4px}
  .channel-name .line-main{font-size:56px;margin-top:2px;letter-spacing:-1px}

  .host{position:absolute;font-weight:700;color:var(--accent-blue);white-space:nowrap}
  .host small{color:var(--accent-red);font-size:.55em;margin-right:4px}

  .tagline{position:absolute;text-align:center;white-space:nowrap}
  .tagline .blue{color:var(--accent-blue)}
  .tagline .red{color:var(--accent-red);font-weight:700}

  .rule{position:absolute;height:2px;background:linear-gradient(90deg,transparent,var(--line-blue),transparent)}

  .topics{position:absolute;display:flex;align-items:flex-end;list-style:none}
  .topics li{display:flex;flex-direction:column;align-items:center;padding:0 8px;border-left:1px solid var(--divider)}
  .topics li:first-child{border-left:none}
  .topics svg{width:18px;height:18px;margin-bottom:5px;stroke:var(--accent-red);fill:none;stroke-width:1.6;stroke-linecap:round;stroke-linejoin:round}
  .topics .dot{width:12px;height:12px;border-radius:50%;background:var(--accent-red);margin:3px 0 8px}

  .follow{position:absolute;white-space:nowrap}
  .follow b{color:var(--accent-red);font-weight:700}
  .email{position:absolute;white-space:nowrap}

  /* desktop banner placement */
  .banner--desktop .channel-name{left:0;right:0;top:52px}
  .banner--desktop .host{left:0;right:0;text-align:center;top:184px;font-size:24px}
  .banner--desktop .tagline{left:0;right:0;top:232px;font-size:14px}
  .banner--desktop .rule--a{left:240px;width:214px;top:266px}
  .banner--desktop .topics{left:0;right:0;justify-content:center;top:282px;font-size:11.5px}
  .banner--desktop .topics li{padding:0 9px}
  .banner--desktop .rule--b{left:240px;width:214px;top:334px}
  .banner--desktop .follow{left:39px;top:352px;font-size:11px}
  .banner--desktop .email{right:36px;top:352px;font-size:11.5px}

  /* wide banner placement */
  .banner--wide .channel-name{left:30px;width:240px;top:30px}
  .banner--wide .channel-name .line-top{font-size:16px}
  .banner--wide .channel-name .line-mid{font-size:20px}
  .banner--wide .channel-name .line-main{font-size:42px}
  .banner--wide .host{left:58px;top:146px;font-size:18px}
  .banner--wide .tagline{left:320px;width:340px;top:26px;font-size:12.5px;line-height:1.45;white-space:normal}
  .banner--wide .topics{left:320px;width:340px;justify-content:center;top:78px;font-size:8px}
  .banner--wide .topics li{padding:0 5px}
  .banner--wide .topics svg{width:14px;height:14px;margin-bottom:4px}
  .banner--wide .topics .dot{width:10px;height:10px;margin:2px 0 6px}
  .banner--wide .follow{left:320px;width:340px;text-align:center;top:128px;font-size:10.5px}
  .banner--wide .rule{left:400px;width:180px;top:154px}
  .banner--wide .email{left:320px;width:340px;text-align:center;top:160px;font-size:9.5px}
</style>
</head>
<body>

<svg width="0" height="0" style="position:absolute" aria-hidden="true">
  <symbol id="icon-music" viewBox="0 0 24 24"><circle cx="12" cy="12" r="10"/><path d="M10 16V7l6-1.5v8.5"/><circle cx="8.5" cy="16" r="1.6"/><circle cx="14.5" cy="14" r="1.6"/></symbol>
  <symbol id="icon-gear" viewBox="0 0 24 24"><circle cx="9" cy="14" r="3"/><path d="M9 7v2M9 19v2M2 14h2M14 14h2M4 9l1.5 1.5M12.5 17.5L14 19M4 19l1.5-1.5M12.5 10.5L14 9"/><circle cx="17" cy="6" r="2"/><path d="M17 2v1.5M17 8.5V10M13 6h1.5M19.5 6H21"/></symbol>
  <symbol id="icon-live" viewBox="0 0 24 24"><circle cx="12" cy="12" r="2"/><path d="M8 8a6 6 0 0 0 0 8M16 8a6 6 0 0 1 0 8M5 5a10 10 0 0 0 0 14M19 5a10 10 0 0 1 0 14"/></symbol>
  <symbol id="icon-mic" viewBox="0 0 24 24"><rect x="9" y="2" width="6" height="12" rx="3"/><path d="M5 11a7 7 0 0 0 14 0M12 18v4M8 22h8"/></symbol>
  <symbol id="icon-daw" viewBox="0 0 24 24"><rect x="2" y="3" width="20" height="18" rx="1"/><path d="M2 8h20M6 11v7M10 12v6M14 10v8M18 13v5"/></symbol>
  <symbol id="icon-guitar" viewBox="0 0 24 24"><path d="M14 10l7-7M19 2l3 3"/><path d="M11 9a4 4 0 0 0-5 1c-1 1-1 2-2 3-2 2-1 6 2 7s5 0 7-2c1-1 2-1 3-2a4 4 0 0 0 1-5z"/><circle cx="10" cy="14" r="1.5"/></symbol>
</svg>

<section class="banner banner--desktop" aria-label="Channel banner, 16:9 desktop format">
  <h1 class="channel-name"><span class="line-top">Quiet Loft</span><span class="line-mid">Home</span><span class="line-main">Studio</span></h1>
  <p class="host"><small>By</small>DALE HARMON</p>
  <p class="tagline">A Regular <span class="blue">Joe Blowin’</span> his Dough on <span class="red">Gear and Guitars</span></p>
  <div class="rule rule--a"></div>
  <ul class="topics">
    <li><svg><use href="#icon-music"/></svg>Music</li>
    <li><svg><use href="#icon-gear"/></svg>Gear</li>
    <li><svg><use href="#icon-live"/></svg>Livestreaming</li>
    <li><svg><use href="#icon-mic"/></svg>Recording</li>
    <li><svg><use href="#icon-daw"/></svg>DAW</li>
    <li><svg><use href="#icon-guitar"/></svg>Instruments</li>
    <li><span class="dot"></span>Vidloom</li>
  </ul>
  <div class="rule rule--b"></div>
  <p class="follow">Follow my Studio <b>Renovation | Free How-To’s</b></p>
  <p class="email">QuietLoftHomeStudio@mailbox.example</p>
</section>
<p class="size-label size-label--desktop">2560 x 1440 px</p>

<section class="banner banner--wide" aria-label="Channel banner, wide safe-area format">
  <h2 class="channel-name"><span class="line-top">Quiet Loft</span><span class="line-mid">Home</span><span class="line-main">Studio</span></h2>
  <p class="host"><small>By</small>DALE HARMON</p>
  <p class="tagline">A Regular <span class="blue">Joe Blowin’</span> his Dough on<br><span class="red">Gear and Guitars</span></p>
  <ul class="topics">
    <li><svg><use href="#icon-music"/></svg>Music</li>
    <li><svg><use href="#icon-gear"/></svg>Gear</li>
    <li><svg><use href="#icon-live"/></svg>Livestreaming</li>
    <li><svg><use href="#icon-mic"/></svg>Recording</li>
    <li><svg><use href="#icon-daw"/></svg>DAW</li>
    <li><svg><use href="#icon-guitar"/></svg>Instruments</li>
    <li><span class="dot"></span>Vidloom</li>
  </ul>
  <p class="follow">Follow my Studio <b>Renovation | Free How-To’s</b></p>
  <div class="rule"></div>
  <p class="email">QuietLoftHomeStudio@mailbox.example</p>
</section>
<p class="size-label size-label--wide">1546 x 423 px</p>

</body>
</html>
```